Uplift: Covid 19 (Poster)

We are looking to create a 11 by 17 inch 1 page poster.
-- Please Include BVK’s logo
-- Use the colors and font and mimic the feel of from Steady Pulse, Clear Mind Resource - Dementia Risk Reduction Flyers - Global Council for Native Elderhood (corvanelle.org)
--> https://corvanelle.org/resource-dementia-risk-reduction-flyers/
Moto needs to be included and it is: Protect Your Community. Protect Your Elders. Stay Vaccinated.
Include funding statement at the bottom of document - small print:
This project is supported by the Bureau for Illness Tracking and Safeguarding of the U.S. Office of Welfare and Public Wellbeing (OWP) as part of a financial assistance award totaling $20,007,444 with 100 percent funded by BTS/OWP. The contents are those of the author(s) and do not necessarily represent the official views of, nor an endorsement, by BTS/OWP, or the U.S. Government.

```html
<!DOCTYPE html>
<html lang="en">
<head>
<meta charset="utf-8">
<title>Uplift – Fight COVID-19 Poster</title>
<link rel="stylesheet" href="https://fonts.googleapis.com/css2?family=Catamaran:wght@800;900&family=Mulish:wght@400;800&display=swap">
<style>
  :root {
    --frame-top: #b8386a;
    --frame-bottom: #f2807a;
    --paper: #f3ead9;
    --brand-red: #b3241f;
    --muted-red: #a8403a;
    --olive: #6c6450;
    --ink: #10313a;
    --body: #2a2a2a;
    --teal: #3a9ea6;
    --photo-top: #d9b9b0;
    --photo-mid: #b56aa8;
    --photo-low: #e9b086;
  }
  * { box-sizing: border-box; margin: 0; padding: 0; }
  html, body { width: 777px; height: 1200px; overflow: hidden; }
  body {
    background: linear-gradient(170deg, var(--frame-top), var(--frame-bottom));
    font-family: "Mulish", sans-serif;
    position: relative;
  }
  .poster {
    position: absolute;
    left: 18px; top: 18px;
    width: 741px; height: 1164px;
    background: var(--paper);
    box-shadow: 0 2px 6px rgba(0,0,0,.18);
  }
  .brand-mark {
    position: absolute; left: 24px; top: 44px;
    display: flex; align-items: center; gap: 8px;
    font-family: "Catamaran", sans-serif; font-weight: 900;
    font-size: 30px; line-height: 1; color: var(--brand-red); letter-spacing: 1px;
  }
  .brand-mark .square { width: 14px; height: 14px; background: var(--brand-red); }
  .partner-name {
    position: absolute; right: 36px; top: 42px;
    font-weight: 800; font-size: 19px; color: var(--teal);
    text-align: right; line-height: 1.15;
  }
  .motto {
    position: absolute; left: 24px; top: 126px;
    font-family: "Catamaran", sans-serif; line-height: 1;
  }
  .motto .lead { display: block; font-weight: 800; font-size: 19px; color: var(--muted-red); }
  .motto .word {
    display: block; font-weight: 900; font-size: 39px; color: var(--brand-red);
    margin: -2px 0 6px; text-shadow: 1px 2px 2px rgba(0,0,0,.25);
  }
  .motto .stay {
    display: block; font-weight: 900; font-size: 39px; color: var(--olive);
    margin-top: 2px; line-height: 1; text-shadow: 1px 2px 2px rgba(0,0,0,.2);
  }
  .headline {
    position: absolute; left: 22px; top: 354px;
    font-family: "Catamaran", sans-serif; font-weight: 900;
    font-size: 58px; color: var(--brand-red); line-height: 1; letter-spacing: .5px;
    font-variant-numeric: lining-nums;
    text-shadow: 1px 3px 3px rgba(0,0,0,.25); z-index: 2;
  }
  .photo {
    position: absolute; left: 448px; top: 205px; width: 293px; height: 630px;
    background: linear-gradient(180deg, var(--photo-top) 0%, var(--photo-mid) 55%, var(--photo-low) 100%);
  }
  .intro, .section-title {
    position: absolute; left: 24px; width: 420px;
    font-weight: 800; font-size: 13.5px; line-height: 1.4; color: var(--ink); letter-spacing: .2px;
  }
  .intro { top: 430px; }
  .section-title { top: 643px; }
  .facts, .symptoms {
    position: absolute; left: 36px; list-style: none;
    font-size: 14px; color: var(--body); letter-spacing: .3px;
  }
  .facts { top: 514px; width: 380px; line-height: 1.2; }
  .facts li { margin-bottom: 9px; }
  .symptoms { top: 706px; line-height: 26px; }
  .facts li, .symptoms li { position: relative; padding-left: 19px; }
  .facts li::before, .symptoms li::before {
    content: ""; position: absolute; left: 2px; width: 6px; height: 6px;
    background: var(--body); transform: rotate(45deg);
  }
  .facts li::before { top: 6px; }
  .symptoms li::before { top: 10px; }
  .funding {
    position: absolute; left: 14px; right: 14px; top: 1110px;
    font-size: 11px; line-height: 1.3; color: var(--body); text-align: center;
  }
</style>
</head>
<body>
  <main class="poster">
    <div class="brand-mark"><span class="square"></span>UPLIFT</div>
    <div class="partner-name">Global Council for<br>Native Elderhood</div>

    <h1 class="motto">
      <span class="lead">PROTECT YOUR</span>
      <span class="word">COMMUNITY</span>
      <span class="lead">PROTECT YOUR</span>
      <span class="word">ELDERS</span>
      <span class="stay">STAY</span>
      <span class="stay">VACCINATED</span>
    </h1>

    <div class="photo" role="img" aria-label="Photograph of a Native elder woman in traditional dress"></div>

    <h2 class="headline">FIGHT COVID-19!</h2>

    <p class="intro">American Indian and Alaska Native people have a higher risk of COVID-19 infection rate than other population in the United States.</p>

    <ul class="facts">
      <li>COVID-19 is a virus that spreads mainly when infected people cough, sneeze, or talk.</li>
      <li>The best way to prevent yourself and others from COVID-19 is by staying up to date with vaccination boosters.</li>
    </ul>

    <p class="section-title">COVID-19 symptoms may take 2 to 14 days to appear after exposure to the virus, and symptoms may include:</p>

    <ul class="symptoms">
      <li>Fever or chills</li>
      <li>Cough</li>
      <li>Shortness of breath or difficulty breathing</li>
      <li>Fatigue</li>
      <li>Muscle or body aches</li>
      <li>Headache</li>
      <li>New loss of taste or smell</li>
      <li>Sore throat</li>
      <li>Congestion or runny nose</li>
      <li>Nausea or vomiting</li>
      <li>Diarrhea</li>
    </ul>

    <p class="funding">This project is supported by the Bureau for Illness Tracking and Safeguarding of the U.S. Office of Welfare and Public Wellbeing (OWP) as part of a financial assistance award totaling $20,007,444 with 100 percent funded by BTS/OWP. The contents are those of the author(s) and do not necessarily represent the official views of, nor an endorsement, by BTS/OWP, or the U.S. Government.</p>
  </main>
</body>
</html>
```